Laboratory Pain Managment Brochure

I want a simple easy to read brochure for doctors. My toxicology lab is in the pain management arena. We provide urine drug monitoring to ensure patients are taking their medication properly. I would like a few photos of adults, doctors, nurses and a happy family. Also, feel free to add a logo that would describe this type of testing

Running theme like " Successfully serving North Dakota since 1996 "

Cover Page # 1

Brilliant photo with Corvella Diagnostics

Would like a running theme of being Corvella being a North Dakota based lab

Page # 2

Corvella Labs has been successfully serving North Dakota since 1996. Dr. Gavin Tellemy, President of Corvella Lab, has over 25 years of medical experience doing research for Brindle University and The University of Parkmoor. In addition, he has worked with clinics giving him a comprehensive understanding of drug testing. It is Corvella Lab mission to supply the best service for our costumers by understanding their needs so they can provide the best possible patient care.

Corvella Features:
•24 – 48 Hour Turnaround Time
•Customer Satisfaction is Our Number 1 Priority
•Capable of Billing all Major Insurance Companies
•Thorough Drug Testing Capabilities Including K2/Spice testing
•Apply Lean Process Control to Supply the best Quality of Analysis
•Easy and Convenient Web-based Interface
•Easy and Customizable Reporting
-The Vexlo is state of the art technology that uses ion entrapment to give better quantitative results. This gives us the ability to detect for more drugs at a higher accuracy.

Why test: Page # 2

Why Monitor Prescription Drug Usage? Prescription drug abuse is the use of medication without a prescription, in a way other than prescribed, or for the experience or feeling elicited. According to several national surveys, prescription medications, such as those used to treat pain, attention deficit disorders, and anxiety, are being abused at a rate second only to marijuana among illicit drug users. The consequences of this abuse have been steadily worsening, reflected in increased treatment admissions, emergency room visits, and overdose deaths.

Can you tell if your patient is taking his/her medication properly?
Even though monitoring your patients behavior is important it is not adequate to know if the patient is misusing their medications. Monitoring the patients behavior as well as drug monitoring testing will give you the most insight into your patients drug usage.

There are many reasons why pain patients may not be taking their medication as prescribed:
•Due to fear of addiction will not take the medication.
•Compulsive use because of addiction.
•Sell the medication to someone else for profit.
•Abuse the medication intentionally

FWRAB's Dosage Integrity Safeguard Plan
The 2011 Dosage Integrity Safeguard Plan expands upon the Harlow Administration's Federal Substance Oversight Agenda and includes action in four major areas to reduce prescription drug abuse:

•Education. A crucial first step in tackling the problem of prescription drug abuse is to educate parents, youth, and patients about the dangers of abusing prescription drugs, while requiring prescribers to receive education on the appropriate and safe use, and proper storage and disposal of prescription drugs.
•Monitoring. Implement prescription drug monitoring programs (PDMPs) in every state to reduce “doctor shopping” and diversion, and enhance PDMPs to make sure they can share data across states and are used by healthcare providers.
•Proper Medication Disposal. Develop convenient and environmentally responsible prescription drug disposal programs to help decrease the supply of unused prescription drugs in the home.
•Enforcement. Provide law enforcement with the tools necessary to eliminate improper prescribing practices and stop pill mills.

References
1.(2011, October). Retrieved November 2012, from BSRC: Bureau of Substance Research Councils: http://www.example-substancebureau.test/sites/default/files/rrdosage.pdf
2.Commun Care Rev. 2009 Aug;12(4):185-90. doi: 10.5555/ccr.2009.0042
3. http://www.example-federaloffice.test/fwrab/dosage-integrity

Page # 3 a list of all four panels we offer....... see attachment and use title of panel in the tabs at the bottom of the excel sheet

Back cover Page # 4 ..... brilliant picture..... North Dakota based lab

Corvella Diagnostics, Inc.
482 Larkfield Ave. E
Williston, ND 58934
ph: (701) 555-0143
www.corvellalab.test

I have removed one stat and added another...... please see the references section

Thank you

Target Market(s)

Pain Managment doctors, internal medicine doctors, general practioners, nuerologist, rehab centers, detox facility, hospitals, just about any doctor that prescribes schedule 2 narcotics

Industry/Entity Type

Healthcare

Requirements
Must have
• Back page I want the family picture with a caption reading

We view your patients like family

```html
<!DOCTYPE html>
<html lang="en">
<head>
<meta charset="utf-8">
<title>Corvella Labs – Inside Spread</title>
<link rel="stylesheet" href="https://fonts.googleapis.com/css2?family=Gelasio:ital,wght@0,400;0,700;1,400&display=swap">
<style>
:root{
  --blue:#1b9bd7;
  --ink:#2b2b2b;
  --edge:#dcedf7;
  --paper:#ffffff;
  --rule:#b9d9ec;
}
*{box-sizing:border-box;margin:0;padding:0}
html,body{width:1200px;height:848px;overflow:hidden;background:var(--paper)}
body{font-family:"Gelasio",Georgia,serif;color:var(--ink);position:relative;
  background:linear-gradient(90deg,var(--paper) 0,var(--paper) 1080px,var(--edge) 1200px)}
.abs{position:absolute}
p,li{font-size:12.4px;line-height:15.6px}
.just{text-align:justify}
ul,ol{list-style:none}
.bullets li{padding-left:10px;text-indent:-10px}
.bullets li::before{content:"• "}
h2.section{color:var(--blue);font-weight:700;font-size:21px;line-height:26px}

.intro{left:18px;top:20px;width:366px}
.photo{left:0;top:163px;width:408px;height:242px;
  background:linear-gradient(120deg,#dfeef8 0%,#a9d2ec 45%,#5fb0df 100%)}
.features-title{left:18px;top:417px}
.features{left:18px;top:451px;width:380px}
.features li{line-height:15.4px}
.indent{padding-left:12px}
.why-title{left:18px;top:654px}
.why{left:18px;top:686px;width:366px}

.middle{left:420px;width:364px}
.q{top:20px}
.reasons-intro{top:117px}
.reasons{top:164px}
.plan-band{left:408px;top:242px;width:392px;height:106px;background:var(--blue);
  color:#fff;font-weight:700;font-size:19px;line-height:24px;padding:23px 14px 0 12px}
.plan-intro{top:352px;left:414px;width:372px}
.plan-areas{top:414px;left:414px;width:372px}
.refs{left:412px;top:648px;width:376px;border:1px solid var(--rule);padding:5px 8px 6px;background:#fff}
.refs h3{font-style:italic;font-weight:700;font-size:9.5px;line-height:12px}
.refs li{font-style:italic;font-size:8.6px;line-height:11px;padding-left:10px;text-indent:-10px}

.panel-title{left:800px;width:258px;height:32px;background:var(--blue);color:#fff;
  border-radius:0 16px 16px 0;font-weight:700;font-size:19px;line-height:32px;padding-left:20px}
.col{width:182px;display:flex;flex-direction:column}
.test{background:#fff;border:1px solid var(--rule);margin-bottom:5px}
.test-head{background:var(--blue);color:#fff;font-weight:700;font-size:8px;line-height:9.5px;
  display:flex;justify-content:space-between;padding:3px 4px 2px}
.test-head span:last-child{text-align:center;width:62px}
.row{display:flex;justify-content:space-between;font-size:8.2px;line-height:9.6px;padding:0 4px}
.row:first-of-type{padding-top:2px}
.row:last-child{padding-bottom:2px}
.row span:last-child{width:62px}
.gap{margin-bottom:9px}
</style>
</head>
<body>

<p class="abs intro just">Corvella Labs has been successfully serving North Dakota since 1996. Dr. Gavin Tellemy, President of Corvella Lab, has over 25 years of medical experience doing research for Brindle University and The University of Parkmoor. In addition, he has worked with clinics giving him a comprehensive understanding of drug testing. It is Corvella Lab mission to supply the best service for our costumers by understanding their needs so they can provide the best possible patient care.</p>

<div class="abs photo" role="img" aria-label="Photo of two lab scientists in white coats working with sample tubes and a microscope"></div>

<h2 class="abs section features-title">Corvella Features:</h2>
<ul class="abs bullets features">
  <li>24 – 48 Hour Turnaround Time</li>
  <li>Customer Satisfaction is Our Number 1 Priority</li>
  <li>Capable of Billing all Major Insurance Companies</li>
  <li>Thorough Drug Testing Capabilities Including<br><span class="indent">K2/Spice testing</span></li>
  <li>Apply Lean Process Control to Supply the best<br><span class="indent">Quality of Analysis</span></li>
  <li>Easy and Convenient Web-based Interface</li>
  <li>Easy and Customizable Reporting</li>
  <li>The Vexlo is state of the art technology that uses ion<br><span class="indent">entrapment to give better quantitative results. This gives</span><br><span class="indent">us the ability to detect for more drugs at a higher accuracy.</span></li>
</ul>

<h2 class="abs section why-title">Why test</h2>
<p class="abs why just">Why Monitor Prescription Drug Usage? Prescription drug abuse is the use of medication without a prescription, in a way other than prescribed, or for the experience or feeling elicited. According to several national surveys, prescription medications, such as those used to treat pain, attention deficit disorders, and anxiety, are being abused at a rate second only to marijuana among illicit drug users. The consequences of this abuse have been steadily worsening, reflected in increased treatment admissions, emergency room visits, and overdose deaths.</p>

<p class="abs middle q">Can you tell if your patient is taking his/her medication properly?<br>Even though monitoring your patients behavior is important it is not adequate to know if the patient is misusing their medications. Monitoring the patients behavior as well as drug monitoring testing will give you the most insight into your patients drug usage.</p>
<p class="abs middle reasons-intro">There are many reasons why pain patients may not be taking their medication as prescribed:</p>
<ul class="abs middle bullets reasons">
  <li>Due to fear of addiction will not take the medication.</li>
  <li>Compulsive use because of addiction.</li>
  <li>Sell the medication to someone else for profit.</li>
  <li>Abuse the medication intentionally</li>
</ul>

<h2 class="abs plan-band">FWRAB's Dosage Integrity Safeguard Plan</h2>
<p class="abs plan-intro just">The 2011 Dosage Integrity Safeguard Plan expands upon the Harlow Administration's Federal Substance Oversight Agenda and includes action in four major areas to reduce prescription drug abuse:</p>
<ul class="abs bullets plan-areas just">
  <li>Education. A crucial first step in tackling the problem of prescription drug abuse is to educate parents, youth, and patients about the dangers of abusing prescription drugs, while requiring prescribers to receive education on the appropriate and safe use, and proper storage and disposal of prescription drugs.</li>
  <li>Monitoring. Implement prescription drug monitoring programs (PDMPs) in every state to reduce “doctor shopping” and diversion, and enhance PDMPs to make sure they can share data across states and are used by healthcare providers.</li>
  <li>Proper Medication Disposal. Develop convenient and environmentally responsible prescription drug disposal programs to help decrease the supply of unused prescription drugs in the home.</li>
  <li>Enforcement. Provide law enforcement with the tools necessary to eliminate improper prescribing practices and stop pill mills.</li>
</ul>

<div class="abs refs">
  <h3>References</h3>
  <ol>
    <li>1. (2011, October). Retrieved November 2012, from BSRC: Bureau of Substance Research Councils: http://www.example-substancebureau.test/sites/default/files/rrdosage.pdf</li>
    <li>2. Commun Care Rev. 2009 Aug;12(4):185-90. doi: 10.5555/ccr.2009.0042</li>
    <li>3. http://www.example-federaloffice.test/fwrab/dosage-integrity</li>
  </ol>
</div>

<h2 class="abs panel-title" style="top:20px">Physician Panel 1</h2>
<div class="abs col" style="left:818px;top:65px">
  <div class="test"><div class="test-head"><span>Amphetamines (3)</span><span>Recommended Cut-off</span></div>
    <div class="row"><span>Amphetamine</span><span>50 ng/mL</span></div>
    <div class="row"><span>Methamphetamine</span><span>50 ng/mL</span></div>
    <div class="row"><span>MDMA</span><span>50 ng/mL</span></div></div>
  <div class="test"><div class="test-head"><span>Benzodiazepines (9)</span><span>Recommended Cut-off</span></div>
    <div class="row"><span>Alprazolam 1</span><span>50 ng/mL</span></div>
    <div class="row"><span>Clonazepam 1</span><span>50 ng/mL</span></div>
    <div class="row"><span>Diazepam 1</span><span>50 ng/mL</span></div>
    <div class="row"><span>Flurazepam 1</span><span>50 ng/mL</span></div>
    <div class="row"><span>Hydroxyalprazolam 1</span><span>50 ng/mL</span></div>
    <div class="row"><span>Lorazepam 1</span><span>50 ng/mL</span></div>
    <div class="row"><span>Nordiazepam 1</span><span>50 ng/mL</span></div>
    <div class="row"><span>Oxazepam 1</span><span>50 ng/mL</span></div>
    <div class="row"><span>Temazepam 1</span><span>50 ng/mL</span></div></div>
  <div class="test"><div class="test-head"><span>Buprenorphine (2)</span><span>Recommended Cut-off</span></div>
    <div class="row"><span>Buprenorphine</span><span>2 ng/mL</span></div>
    <div class="row"><span>Norbuprenorphine</span><span>10ng/mL</span></div></div>
  <div class="test"><div class="test-head"><span>Cannabinoids (1)</span><span>Recommended Cut-off</span></div>
    <div class="row"><span>THC 1</span><span>20 ng/mL</span></div></div>
  <div class="test"><div class="test-head"><span>Cocaine (1)</span><span>Recommended Cut-off</span></div>
    <div class="row"><span>Benzoylecgonine 1</span><span>30 ng/mL</span></div></div>
  <div class="test"><div class="test-head"><span>Ethyl Glucuronide (1)</span><span>Recommended Cut-off</span></div>
    <div class="row"><span>Etg 1</span><span>500 ng/mL</span></div></div>
</div>
<div class="abs col" style="left:1006px;top:65px">
  <div class="test gap"><div class="test-head"><span>Fentanyl (2)</span><span>Recommended Cut-off</span></div>
    <div class="row"><span>Fentanyl 1</span><span>0.5 ng/mL</span></div>
    <div class="row"><span>Norfentanyl 1</span><span>0.5 ng/mL</span></div></div>
  <div class="test gap"><div class="test-head"><span>Methadone (2)</span><span>Recommended Cut-off</span></div>
    <div class="row"><span>Methadone 1</span><span>100 ng/mL</span></div>
    <div class="row"><span>EDDP 1</span><span>100 ng/mL</span></div></div>
  <div class="test"><div class="test-head"><span>Opiates (7)</span><span>Recommended Cut-off</span></div>
    <div class="row"><span>6-MAM 1</span><span>20 ng/mL</span></div>
    <div class="row"><span>Codeine 1</span><span>50 ng/mL</span></div>
    <div class="row"><span>Hydrocodone 1</span><span>50 ng/mL</span></div>
    <div class="row"><span>Hydromorphone 1</span><span>50 ng/mL</span></div>
    <div class="row"><span>Morphine 1</span><span>50 ng/mL</span></div>
    <div class="row"><span>Oxycodone 1</span><span>50 ng/mL</span></div>
    <div class="row"><span>Oxymorphone 1</span><span>50 ng/mL</span></div></div>
  <div class="test"><div class="test-head"><span>Muscle Relaxant (2)</span><span>Recommended Cut-off</span></div>
    <div class="row"><span>Carisoprodol 1</span><span>100 ng/mL</span></div>
    <div class="row"><span>Meprobamate 1</span><span>100 ng/mL</span></div></div>
  <div class="test"><div class="test-head"><span>Tramadol</span><span>Recommended Cut-off</span></div>
    <div class="row"><span>Tramadol 1</span><span>125 ng/mL</span></div></div>
</div>

<h2 class="abs panel-title" style="top:427px">Physician Panel 2</h2>
<div class="abs col" style="left:818px;top:471px">
  <div class="test"><div class="test-head"><span>Amphetamines (3)</span><span>Recommended Cut-off</span></div>
    <div class="row"><span><b>Amphetamine</b></span><span>50 ng/mL</span></div>
    <div class="row"><span><b>Methamphetamine</b></span><span>50 ng/mL</span></div>
    <div class="row"><span><b>MDMA</b></span><span>50 ng/mL</span></div></div>
  <div class="test"><div class="test-head"><span>Benzodiazepines (9)</span><span>Recommended Cut-off</span></div>
    <div class="row"><span>Alprazolam 1</span><span>50 ng/mL</span></div>
    <div class="row"><span>Clonazepam 1</span><span>50 ng/mL</span></div>
    <div class="row"><span>Diazepam 1</span><span>50 ng/mL</span></div>
    <div class="row"><span>Flurazepam 1</span><span>50 ng/mL</span></div>
    <div class="row"><span>Hydroxyalprazolam 1</span><span>50 ng/mL</span></div>
    <div class="row"><span>Lorazepam 1</span><span>50 ng/mL</span></div>
    <div class="row"><span>Nordiazepam 1</span><span>50 ng/mL</span></div>
    <div class="row"><span>Oxazepam 1</span><span>50 ng/mL</span></div>
    <div class="row"><span>Temazepam 1</span><span>50 ng/mL</span></div></div>
  <div class="test"><div class="test-head"><span>Buprenorphine (2)</span><span>Recommended Cut-off</span></div>
    <div class="row"><span>Buprenorphine</span><span>2 ng/mL</span></div>
    <div class="row"><span>Norbuprenorphine</span><span>10ng/mL</span></div></div>
  <div class="test"><div class="test-head"><span>Cannabinoids (1)</span><span>Recommended Cut-off</span></div>
    <div class="row"><span>THC 1</span><span>20 ng/mL</span></div></div>
  <div class="test"><div class="test-head"><span>Cocaine (1)</span><span>Recommended Cut-off</span></div>
    <div class="row"><span>Benzoylecgonine 1</span><span>30 ng/mL</span></div></div>
  <div class="test"><div class="test-head"><span>Ethyl Glucuronide (1)</span><span>Recommended Cut-off</span></div>
    <div class="row"><span>Etg 1</span><span>500 ng/mL</span></div></div>
</div>
<div class="abs col" style="left:1006px;top:471px">
  <div class="test gap"><div class="test-head"><span>Fentanyl (2)</span><span>Recommended Cut-off</span></div>
    <div class="row"><span>Fentanyl 1</span><span>0.5 ng/mL</span></div>
    <div class="row"><span>Norfentanyl 1</span><span>0.5 ng/mL</span></div></div>
  <div class="test gap"><div class="test-head"><span>Methadone (2)</span><span>Recommended Cut-off</span></div>
    <div class="row"><span>Methadone 1</span><span>100 ng/mL</span></div>
    <div class="row"><span>EDDP 1</span><span>100 ng/mL</span></div></div>
  <div class="test"><div class="test-head"><span>Opiates (7)</span><span>Recommended Cut-off</span></div>
    <div class="row"><span>6-MAM 1</span><span>20 ng/mL</span></div>
    <div class="row"><span>Codeine 1</span><span>50 ng/mL</span></div>
    <div class="row"><span>Hydrocodone 1</span><span>50 ng/mL</span></div>
    <div class="row"><span>Hydromorphone 1</span><span>50 ng/mL</span></div>
    <div class="row"><span>Morphine 1</span><span>50 ng/mL</span></div>
    <div class="row"><span>Oxycodone 1</span><span>50 ng/mL</span></div>
    <div class="row"><span>Oxymorphone 1</span><span>50 ng/mL</span></div></div>
</div>

</body>
</html>
```